Business card for job seeker professional

Hi. I'm a sale and marketing professional who's just moved to Australia and looking for a job. I would like to have a business card designed for me, which I can use for job interviews/networking. Given Pronexa increasing importance in the job market, I would like my public profile link (http://au.pronexa.com/in/dorianmalvek/) to be incorporated into my details.

```html
<!DOCTYPE html>
<html lang="en">
<head>
<meta charset="utf-8">
<title>Dorian Malvek – Business Card</title>
<link href="https://fonts.googleapis.com/css2?family=Carlito&family=Tinos&display=swap" rel="stylesheet">
<style>
  :root {
    --paper: #ffffff;
    --ink: #1b1b1a;
    --cream: #ebeae3;
    --sage: #e1e1d3;
    --sage-deep: #dcdccd;
    --edge: #9a9a8e;
    --accent: #ffa800;
    --light-text: #ffffff;
    --body-text: #1e1e1e;
  }
  html, body {
    margin: 0;
    padding: 0;
    overflow: hidden;
    background: var(--paper);
  }
  .card {
    position: relative;
    width: 1200px;
    height: 681px;
    overflow: hidden;
    background: var(--paper);
  }
  .card-shapes {
    position: absolute;
    inset: 0;
    width: 1200px;
    height: 681px;
  }
  .band-dark { fill: var(--ink); }
  .field-cream { fill: var(--cream); stroke: var(--edge); stroke-width: 0.6; }
  .field-sage { fill: var(--sage); stroke: var(--edge); stroke-width: 0.6; }
  .field-sage-deep { fill: var(--sage-deep); stroke: var(--edge); stroke-width: 0.6; }

  .brand-name {
    position: absolute;
    left: 238px;
    top: 262px;
    margin: 0;
    font-family: "Carlito", "Calibri", sans-serif;
    font-size: 60px;
    font-weight: 700;
    color: var(--accent);
  }
  .holder-name {
    position: absolute;
    left: 753px;
    top: 48px;
    margin: 0;
    font-family: "Carlito", "Calibri", sans-serif;
    font-weight: 400;
    font-size: 48px;
    line-height: 1;
    color: var(--light-text);
  }
  .holder-role {
    position: absolute;
    left: 760px;
    top: 110px;
    margin: 0;
    font-family: "Tinos", "Times New Roman", serif;
    font-size: 31px;
    line-height: 1;
    color: var(--light-text);
  }
  .contact-list {
    position: absolute;
    left: 633px;
    top: 392px;
    margin: 0;
    padding: 0;
    list-style: none;
    font-family: "Tinos", "Times New Roman", serif;
    font-size: 29px;
    line-height: 35.4px;
    color: var(--body-text);
  }
  .contact-item {
    display: flex;
    align-items: baseline;
  }
  .contact-label {
    width: 173px;
  }
  .contact-value {
    margin-left: 14px;
    font-size: 19px;
    white-space: nowrap;
  }
</style>
</head>
<body>
  <div class="card">
    <svg class="card-shapes" viewBox="0 0 916 519" preserveAspectRatio="none" aria-hidden="true">
      <path class="band-dark" d="M175,0 L916,0 L916,162 Q520,230 258,370 L240,410 Q120,345 0,310 L0,100 Z"/>
      <path class="field-cream" d="M916,162 Q520,230 258,370 L240,410 L210,519 L916,519 Z"/>
      <path class="field-sage" d="M0,310 Q120,345 240,410 L210,519 L0,519 Z"/>
      <path class="field-sage-deep" d="M240,410 Q350,455 430,519 L210,519 Z"/>
    </svg>

    <p class="brand-name">Malvek</p>

    <h1 class="holder-name">Dorian Malvek</h1>
    <p class="holder-role">Sales &amp; Marketing</p>

    <ul class="contact-list">
      <li class="contact-item"><span class="contact-label">Tel</span><span class="contact-sep">:</span><span class="contact-value">+61 2 5550 1842</span></li>
      <li class="contact-item"><span class="contact-label">Mob</span><span class="contact-sep">:</span><span class="contact-value">+61 4 5550 3971</span></li>
      <li class="contact-item"><span class="contact-label">Email</span><span class="contact-sep">:</span><span class="contact-value">dorian@malvek.com.au</span></li>
      <li class="contact-item"><span class="contact-label">Website</span><span class="contact-sep">:</span><span class="contact-value">http://au.pronexa.com/in/dorianmalvek/</span></li>
      <li class="contact-item"><span class="contact-label">Fax</span><span class="contact-sep">:</span><span class="contact-value">+61 2 5550 1843</span></li>
      <li class="contact-item"><span class="contact-label">Address</span><span class="contact-sep">:</span><span class="contact-value">12 Harbour Lane, Sydney NSW 2000</span></li>
    </ul>
  </div>
</body>
</html>
```